WEBSITE DESIGN - www.brindolux.com

We need a professional and modern looking website for our business. The current website was only made tentatively and can be viewed (we expect a website MUCH better than this). It needs to be simple and non-cluttered yet look modern and sophisticated. It needs to be very easy to navigate as our tarket market is people over the age of 45. Our logo is attached below and this should be incorporated plus the colours/theme should match this. We don't mind purchasing images online if your design includes these and we like it.

Any other specific questions please enquire as we want to hear them.

Target Market(s)

over 45 age english speaking westerners

Industry/Entity Type

Business

Number of Pages Required

1 page

Requirements
Must have
• -our logo (attached).
• -page tabs as those described (tabs.. but not necessarily each of these pages completed as well although this would be nice).
• -social media logos
• Pages should include: homepage, services, pricing, about us, contact us. There should also be a payments page designed which would link with the other pages but there would be no tab for this.

```html
<!DOCTYPE html>
<html lang="en">
<head>
<meta charset="utf-8">
<title>Brindolux Computer Solutions</title>
<link rel="stylesheet" href="https://fonts.googleapis.com/css2?family=Exo+2:wght@500;600;700&family=Lato:ital,wght@0,400;0,700;0,900;1,400&display=swap">
<style>
:root{
  --orange:#c07a06;
  --orange-dark:#9a6104;
  --ink:#1d1d1d;
  --navy:#1f2a44;
  --text:#333;
  --muted:#666;
  --yellow:#f8d363;
  --teal:#0f2c33;
  --line:#d6d6d6;
  --white:#fff;
}
*{box-sizing:border-box;margin:0;padding:0}
html,body{width:1200px;height:3711px;overflow:hidden}
body{font-family:'Lato',sans-serif;color:var(--text);background:var(--white);position:relative}
.title{font-family:'Exo 2',sans-serif;font-weight:600}
section,header,footer{position:relative;width:1200px;overflow:hidden}

/* top bar */
.topbar{height:45px;background:var(--ink);color:var(--white);display:flex;align-items:center;justify-content:space-between;padding:0 80px}
.topbar .phone{font-size:17px;font-weight:700;display:flex;align-items:center;gap:8px}
.social{display:flex;gap:9px}
.social span{width:28px;height:28px;border-radius:50%;background:var(--white);display:block}
.topbar .social span{background:#e6e6e6}

/* nav */
.nav{height:123px;display:flex;align-items:center;padding:0 80px;font-weight:900;font-size:17px;color:var(--ink);letter-spacing:.5px}
.nav .home{width:28px;margin-left:6px}
.nav .item{padding:0 26px;border-right:1px solid var(--line)}
.nav .item:last-child{border-right:none}
.nav .left,.nav .right{display:flex;align-items:center}
.nav .left{flex:1;gap:0}
.nav .right{flex:1;justify-content:flex-end}
.brand{display:flex;flex-direction:column;align-items:center;gap:6px}
.brand .dot{width:44px;height:44px;border-radius:50%;background:var(--ink)}
.brand .name{font-size:38px;font-weight:400;color:var(--ink);letter-spacing:1px;line-height:1}
.brand .tag{font-size:12px;font-weight:700;color:var(--orange);letter-spacing:2px}

/* hero */
.hero{height:463px;background:linear-gradient(180deg,#6f7a84 0%,#9aa3ab 45%,#4a4d52 72%,#3a2e2a 100%)}
.hero .caption{position:absolute;left:0;right:0;bottom:34px;text-align:center;color:var(--white);font-family:'Exo 2',sans-serif;font-weight:700;font-size:30px;line-height:38px;text-shadow:0 2px 4px rgba(0,0,0,.5)}
.hero .arrow{position:absolute;top:352px}
.hero .arrow.l{left:16px}.hero .arrow.r{right:16px}

/* section headings */
.heading{display:flex;align-items:center;justify-content:center;gap:18px}
.heading .rule{width:120px;height:1px;background:var(--line)}
.heading .pin{width:10px;height:36px;border:2px solid #888;border-radius:5px}
.heading h2{font-family:'Exo 2',sans-serif;font-weight:700;font-size:34px;color:var(--navy)}
.heading h2 em{font-style:normal;color:var(--orange)}

/* welcome */
.welcome{height:376px;padding-top:50px;text-align:center}
.welcome p{width:1060px;margin:46px auto 0;font-size:12.5px;line-height:26px;color:var(--text)}
.btn-outline{display:inline-block;margin-top:40px;border:2px solid var(--orange);color:var(--orange);font-size:15px;padding:7px 26px}

/* why */
.why{height:675px;background:radial-gradient(ellipse at 50% 45%,#1f4a52 0%,var(--teal) 55%,#081a1e 100%);color:var(--white)}
.why .heading{margin-top:56px}
.why .heading h2{color:var(--white)}
.why .heading .pin{border-color:#bbb}
.why .sub{text-align:center;font-weight:700;font-size:16px;margin-top:20px}
.why .art{position:absolute;left:130px;top:240px;width:250px;height:330px;border-radius:50%;background:radial-gradient(circle,rgba(255,255,255,.12),rgba(255,255,255,0) 70%)}
.why .arc{position:absolute;left:300px;top:200px}
.services{position:absolute;left:528px;top:180px;width:520px}
.service{display:flex;gap:20px;margin-bottom:40px;align-items:flex-start}
.service .icon{width:70px;height:70px;border-radius:50%;background:var(--orange);border:3px solid rgba(255,255,255,.7);flex:none;display:flex;align-items:center;justify-content:center}
.service h3{font-size:15px;font-weight:900;letter-spacing:.5px;margin:6px 0 7px}
.service p{font-size:12px;line-height:18px;color:#d9e2e4}

/* stats */
.stats-band{height:537px}
.stats{display:flex;position:absolute;top:1765px;left:0}
.stat{position:absolute;width:170px;text-align:center;top:70px}
.stat svg{display:block;margin:0 auto}
.stat .num{position:absolute;top:0;left:0;width:170px;height:130px;line-height:130px;font-size:38px;font-weight:700;color:var(--ink)}
.stat .label{font-size:20px;color:var(--ink);margin-top:16px;line-height:22px}
.cta{position:absolute;top:340px;left:0;width:1200px;text-align:center}
.cta h3{font-family:'Exo 2',sans-serif;font-weight:700;font-size:34px;color:var(--orange)}
.btn-solid{display:inline-block;background:var(--orange);color:var(--white);font-weight:900;font-size:22px;padding:14px 24px;margin-top:38px;letter-spacing:.5px}

/* pricing */
.pricing{height:666px;background:var(--yellow)}
.pricing .heading{margin-top:60px}
.pricing .heading .rule{background:#c9a84a}
.plans{position:absolute;top:166px;left:79px;display:flex;gap:32px}
.plan{width:322px;height:360px;background:var(--white);box-shadow:0 6px 10px rgba(0,0,0,.15);position:relative;text-align:center}
.plan .head{height:47px;line-height:47px;background:var(--orange);color:var(--white);font-family:'Exo 2',sans-serif;font-weight:600;font-size:24px}
.plan .cur{display:flex;height:35px;background:#2d2d2d;color:var(--white);font-size:14px;font-weight:700}
.plan .cur span{flex:1;line-height:35px;border-right:1px solid #555}
.plan .cur span:last-child{border:none}
.plan .term{display:inline-block;background:var(--orange);color:var(--white);font-size:14px;padding:6px 22px}
.plan ul{list-style:none;margin-top:22px}
.plan li{font-size:15px;line-height:40px;color:var(--text)}
.plan li::before{content:"\2022";margin-right:10px}
.plan .agree{display:flex;align-items:center;justify-content:center;gap:10px;font-size:12px;margin-top:16px}
.plan .box{width:14px;height:14px;border:1px solid #aaa;display:inline-block}
.plan .order{position:absolute;left:96px;bottom:-20px;width:130px;height:32px;line-height:32px;background:var(--orange);color:var(--white);font-weight:900;font-size:15px}
.pricing .note{position:absolute;top:572px;left:150px;width:900px;text-align:center;font-size:13px;line-height:21px;color:var(--text)}

/* contact */
.contact{height:393px}
.contact h2{font-family:'Exo 2',sans-serif;font-weight:700;font-size:24px;color:var(--ink);display:flex;align-items:center;gap:12px}
.contact h2 em{font-style:normal;color:var(--orange)}
.contact .col{position:absolute;top:46px}
.contact .left{left:79px;width:481px}
.contact .right{left:633px;width:488px}
.contact .rule{height:1px;background:var(--line);margin-top:14px}
.contact .intro{font-size:13px;margin-top:24px}
.fields{display:grid;grid-template-columns:1fr 1fr;gap:12px 22px;margin-top:20px}
.field{height:30px;border:1px solid var(--line);font-size:11px;color:var(--muted);padding:8px 8px}
.field.area{grid-column:1/3;height:70px}
.submit{float:right;margin-top:16px;background:var(--orange);color:var(--white);font-weight:900;font-size:14px;padding:7px 18px}
.quote{margin-top:30px;border:1px solid var(--line);padding:22px 26px 26px 40px;font-style:italic;font-size:13px;line-height:24px;color:var(--text);position:relative}
.quote .mark{position:absolute;left:14px;top:10px;font-size:40px;color:#bbb;font-style:normal}
.client{display:flex;align-items:center;gap:110px;margin-top:-10px;padding-left:30px}
.client .avatar{width:86px;height:86px;border-radius:50%;background:#c9c3b8;border:4px solid var(--white);box-shadow:0 0 0 1px var(--line)}
.client .who{color:var(--orange);font-weight:700;font-size:14px;margin-top:30px}

/* map */
.map{height:379px;background:linear-gradient(135deg,#cfe3ef 0%,#e8ebe4 35%,#f2efe6 60%,#d6e7ef 100%)}
.map .pinmark{position:absolute;left:575px;top:142px;width:26px;height:26px;border-radius:50%;background:#e53040;border:5px solid var(--white)}
.office{position:absolute;left:79px;top:0;width:317px;height:379px;background:rgba(30,34,38,.9);color:var(--white);padding:32px 24px;font-size:13px;line-height:20px}
.office .row{display:flex;gap:18px;margin-bottom:26px}
.office .row svg{flex:none;margin-top:2px}
.office b{font-weight:900;font-size:14px}
.office .social{margin-top:18px}
.office .social span{width:30px;height:30px;background:#d0d0d0}

/* footer */
.footer{height:54px;background:var(--orange-dark);color:var(--white);display:flex;align-items:center;justify-content:space-between;padding:0 79px;font-size:13px;font-weight:700}
.cards{display:flex;gap:8px}
.cards span{width:52px;height:30px;background:#f1f1f1;border-radius:3px;display:block}
</style>
</head>
<body>

<header class="topbar">
  <div class="phone">
    <svg width="16" height="16" viewBox="0 0 24 24"><path fill="#fff" d="M6.6 10.8a15 15 0 0 0 6.6 6.6l2.2-2.2c.3-.3.7-.4 1-.2 1.1.4 2.3.6 3.6.6.6 0 1 .4 1 1V20c0 .6-.4 1-1 1A17 17 0 0 1 3 4c0-.6.4-1 1-1h3.5c.6 0 1 .4 1 1 0 1.3.2 2.5.6 3.6.1.3 0 .7-.2 1z"/></svg>
    +1 555 014 2297
  </div>
  <div class="social"><span></span><span></span><span></span><span></span><span></span><span></span></div>
</header>

<nav class="nav">
  <div class="left">
    <svg class="home" width="28" height="34" viewBox="0 0 28 34"><path d="M2 14 14 3l12 11v14H2z" fill="#c07a06"/><rect x="10" y="19" width="8" height="9" fill="#fff"/></svg>
    <span class="item" style="margin-left:20px">ABOUT US</span>
    <span class="item">SERVICES</span>
  </div>
  <div class="brand">
    <span class="dot"></span>
    <span class="name">Brindolux</span>
    <span class="tag">COMPUTER SOLUTIONS</span>
  </div>
  <div class="right">
    <span class="item">PRICING</span>
    <span class="item">CONTACT US</span>
  </div>
</nav>

<section class="hero" role="img" aria-label="Photo of two businessmen in shirts and ties leaping along a track holding laptops, with a city skyline behind them">
  <svg class="arrow l" width="22" height="40" viewBox="0 0 22 40"><path d="M18 4 4 20l14 16" stroke="#fff" stroke-width="3" fill="none"/></svg>
  <svg class="arrow r" width="22" height="40" viewBox="0 0 22 40"><path d="M4 4l14 16L4 36" stroke="#fff" stroke-width="3" fill="none"/></svg>
  <p class="caption">The one stop comprehensive diagnostic &amp; repair station for your<br>computer and connected devices. We'll fix anything!</p>
</section>

<section class="welcome">
  <div class="heading"><span class="rule"></span><span class="pin"></span><h2>Welcome To <em>Brindolux</em></h2><span class="pin"></span><span class="rule"></span></div>
  <p>Lorem ipsum dolor sit amet, consectetuer adipiscing elit, sed diam nonummy nibh euismod tincidunt ut laoreet dolore magna aliquam erat volutpat. Ut wisi enim ad minim veniam, quis nostrud exerci tation ullamcorper suscipit lobortis nisl ut aliquip ex ea commodo consequat. Duis autem vel eum iriure dolor in hendrerit in vulputate velit esse molestie consequat, vel illum dolore eu feugiat nulla facilisis at vero eros et accumsan et iusto odio dignissim qui blandit praesent luptatum zzril delenit augue duis dolore te feugait nulla facilisi.</p>
  <span class="btn-outline">Read More</span>
</section>

<section class="why" role="img" aria-label="Dark teal photo of a computer workshop with circuit traces in the background">
  <div class="heading"><span class="pin"></span><h2>Why We Are The Best</h2><span class="pin"></span></div>
  <p class="sub">The one stop comprehensive diagnostic &amp; repair station for your computer and connected devices. We'll fix anything!</p>
  <div class="art"></div>
  <svg class="arc" width="120" height="400" viewBox="0 0 120 400"><path d="M10 10 A240 240 0 0 1 10 390" stroke="#fff" stroke-width="5" fill="none"/></svg>
  <div class="services">
    <div class="service">
      <span class="icon"><svg width="32" height="32" viewBox="0 0 32 32"><path d="M6 26 20 12m0-6a6 6 0 1 0 6 6" stroke="#fff" stroke-width="3" fill="none"/></svg></span>
      <div><h3>DIAGNOSIS &amp; REPAIR</h3><p>The one stop comprehensive diagnostic &amp; repair station for your<br>computer and connected devices. We'll fix anything!</p></div>
    </div>
    <div class="service">
      <span class="icon"><svg width="32" height="32" viewBox="0 0 32 32"><circle cx="13" cy="11" r="6" fill="#fff"/><path d="M2 28c0-6 5-10 11-10s11 4 11 10z" fill="#fff"/></svg></span>
      <div><h3>SETUP &amp; INSTALL</h3><p>Confused and frustrated with device setup &amp; installation? Leave it to the<br>experts, which means all you've to do is sit back &amp; relax.</p></div>
    </div>
    <div class="service">
      <span class="icon"><svg width="32" height="32" viewBox="0 0 32 32"><circle cx="16" cy="16" r="11" stroke="#fff" stroke-width="3" fill="none"/><path d="M16 16l7-7" stroke="#fff" stroke-width="3"/></svg></span>
      <div><h3>OPTIMIZATION</h3><p>You won't believe it's the same old computer. Your system will work like<br>it did on the day you bought it! No kidding! Anytime, anywhere remote<br>tech help for your home devices.</p></div>
    </div>
    <div class="service">
      <span class="icon"><svg width="32" height="32" viewBox="0 0 32 32"><rect x="4" y="6" width="24" height="17" stroke="#fff" stroke-width="3" fill="none"/><path d="M11 28h10" stroke="#fff" stroke-width="3"/></svg></span>
      <div><h3>WEB DESIGNING</h3><p>We develop the website, we analyse, strategize and assess our client's<br>specific need, requirement, preference and approach. We not only create<br>website - we create a Brand.</p></div>
    </div>
  </div>
</section>

<section class="stats-band">
  <div class="stat" style="left:58px">
    <svg width="130" height="130" viewBox="0 0 130 130"><circle cx="65" cy="65" r="62" stroke="#bbb" stroke-width="2" fill="none"/><circle cx="65" cy="65" r="62" stroke="#c07a06" stroke-width="4" fill="none" stroke-dasharray="100 400" transform="rotate(150 65 65)"/></svg>
    <span class="num">986</span><p class="label">Laptops</p>
  </div>
  <div class="stat" style="left:237px">
    <svg width="130" height="130" viewBox="0 0 130 130"><circle cx="65" cy="65" r="62" stroke="#bbb" stroke-width="2" fill="none"/><circle cx="65" cy="65" r="62" stroke="#c07a06" stroke-width="4" fill="none" stroke-dasharray="60 400" transform="rotate(170 65 65)"/></svg>
    <span class="num">256</span><p class="label">Routers</p>
  </div>
  <div class="stat" style="left:427px">
    <svg width="130" height="130" viewBox="0 0 130 130"><circle cx="65" cy="65" r="62" stroke="#bbb" stroke-width="2" fill="none"/><circle cx="65" cy="65" r="62" stroke="#c07a06" stroke-width="4" fill="none" stroke-dasharray="90 400" transform="rotate(160 65 65)"/></svg>
    <span class="num">867</span><p class="label">Smart Phones</p>
  </div>
  <div class="stat" style="left:608px">
    <svg width="130" height="130" viewBox="0 0 130 130"><circle cx="65" cy="65" r="62" stroke="#bbb" stroke-width="2" fill="none"/><circle cx="65" cy="65" r="62" stroke="#c07a06" stroke-width="4" fill="none" stroke-dasharray="180 400" transform="rotate(130 65 65)"/></svg>
    <span class="num">1904</span><p class="label">Desktops</p>
  </div>
  <div class="stat" style="left:786px">
    <svg width="130" height="130" viewBox="0 0 130 130"><circle cx="65" cy="65" r="62" stroke="#bbb" stroke-width="2" fill="none"/><circle cx="65" cy="65" r="62" stroke="#c07a06" stroke-width="4" fill="none" stroke-dasharray="50 400" transform="rotate(175 65 65)"/></svg>
    <span class="num">511</span><p class="label">Tablets</p>
  </div>
  <div class="stat" style="left:966px">
    <svg width="130" height="130" viewBox="0 0 130 130"><circle cx="65" cy="65" r="62" stroke="#bbb" stroke-width="2" fill="none"/><circle cx="65" cy="65" r="62" stroke="#c07a06" stroke-width="4" fill="none" stroke-dasharray="220 400" transform="rotate(110 65 65)"/></svg>
    <span class="num">2456</span><p class="label">Software<br>Installation</p>
  </div>
  <div class="cta">
    <h3>Call Us Today For Instant Tech Support NOW!</h3>
    <span class="btn-solid">CONTACT NOW!</span>
  </div>
</section>

<section class="pricing">
  <div class="heading"><span class="rule"></span><span class="pin"></span><h2>Our Affordable Prices</h2><span class="pin"></span><span class="rule"></span></div>
  <div class="plans">
    <div class="plan">
      <div class="head">Quick Fix</div>
      <div class="cur"><span>NZD 95</span><span>USD 60*</span><span>GBP 40*</span></div>
      <span class="term">1 Month</span>
      <ul><li>1 Month Tech Support</li><li>For 1 Computer</li><li>24X7 Availability</li></ul>
      <div class="agree"><svg width="16" height="16" viewBox="0 0 16 16"><rect x=".5" y=".5" width="15" height="15" fill="none" stroke="#aaa"/><path d="M3 8l3 3 7-8" stroke="#c07a06" stroke-width="2" fill="none"/></svg>I Agree To The Terms And Conditions</div>
      <span class="order">ORDER NOW</span>
    </div>
    <div class="plan">
      <div class="head">Starter</div>
      <div class="cur"><span>NZD 95</span><span>USD 60*</span><span>GBP 40*</span></div>
      <span class="term">6 Month</span>
      <ul><li>6 Month Tech Support</li><li>6 Month support for the same issue</li><li>24X7 Availability</li></ul>
      <div class="agree"><span class="box"></span>I Agree To The Terms And Conditions</div>
      <span class="order">ORDER NOW</span>
    </div>
    <div class="plan">
      <div class="head">Advance</div>
      <div class="cur"><span>NZD 95</span><span>USD 60*</span><span>GBP 40*</span></div>
      <span class="term">1 Year</span>
      <ul><li>1 Year Tech Support</li><li>Upto 3 Computers &amp; Printers</li><li>Connected Devices with Router</li></ul>
      <div class="agree"><span class="box"></span>I Agree To The Terms And Conditions</div>
      <span class="order">ORDER NOW</span>
    </div>
  </div>
  <p class="note">*The price advertised might not be the same price charged to the credit card account due to exchange rate fluctuations. This means that because we are based in New Zealand we have to convert your purchase to New Zealand dollars at the exchange rate on the day it is processed.</p>
</section>

<section class="contact">
  <div class="col left">
    <h2><svg width="22" height="16" viewBox="0 0 22 16"><rect width="22" height="16" fill="#1d1d1d"/><path d="M1 1l10 8 10-8" stroke="#fff" stroke-width="1.5" fill="none"/></svg>Get In <em>Touch With Us</em></h2>
    <div class="rule"></div>
    <p class="intro">Lorem ipsum dolor sit amet consectetur adipiscing sed dmmy nibh</p>
    <div class="fields">
      <div class="field">First Name</div><div class="field">Last Name</div>
      <div class="field">Phone Number</div><div class="field">Email</div>
      <div class="field area">Your Message</div>
    </div>
    <span class="submit">SUBMIT</span>
  </div>
  <div class="col right">
    <h2><svg width="24" height="20" viewBox="0 0 24 20"><path d="M2 2h14v9H7l-4 4v-4H2z" fill="#1d1d1d"/><path d="M18 6h4v9h-1v3l-3-3h-7v-2h7z" fill="#1d1d1d"/></svg>Client <em>Testimonials</em></h2>
    <div class="rule"></div>
    <div class="quote"><span class="mark">&ldquo;</span>Lorem ipsum dolor sit amet consetug e sed diay nibh euismod tincidunt ut laoreet dolore magna er vol wisi enim ad minim veniam quis nostrud exerci tation enim ipsum dolor sit amet sed dammy nibh euismod tincidunt ut laoreet dolore magna aliqur volpat tiidunt ut laoreet dolore magna aliqur volpat!</div>
    <div class="client"><span class="avatar" role="img" aria-label="Client portrait"></span><span class="who">Mr. Ellis Harmon</span></div>
  </div>
</section>

<section class="map" role="img" aria-label="Street map of central Auckland with the office location marked">
  <span class="pinmark"></span>
  <div class="office">
    <div class="row">
      <svg width="16" height="22" viewBox="0 0 16 22"><path d="M8 0a8 8 0 0 0-8 8c0 6 8 14 8 14s8-8 8-14a8 8 0 0 0-8-8z" fill="#fff"/><circle cx="8" cy="8" r="3" fill="#333"/></svg>
      <div><b>HEAD OFFICE ADDRESS</b><br>Marlow Gardens Tower 1<br>5H/205 Marlow Street, Auckland Central<br>Auckland- 1010 New Zealand</div>
    </div>
    <div class="row">
      <svg width="18" height="14" viewBox="0 0 18 14"><rect width="18" height="14" fill="#fff"/><path d="M1 1l8 6 8-6" stroke="#333" stroke-width="1.5" fill="none"/></svg>
      <div>info@brindolux.com</div>
    </div>
    <div class="row">
      <svg width="16" height="16" viewBox="0 0 24 24"><path fill="#fff" d="M6.6 10.8a15 15 0 0 0 6.6 6.6l2.2-2.2c.3-.3.7-.4 1-.2 1.1.4 2.3.6 3.6.6.6 0 1 .4 1 1V20c0 .6-.4 1-1 1A17 17 0 0 1 3 4c0-.6.4-1 1-1h3.5c.6 0 1 .4 1 1 0 1.3.2 2.5.6 3.6.1.3 0 .7-.2 1z"/></svg>
      <div>+64 7000 3185</div>
    </div>
    <div class="social"><span></span><span></span><span></span><span></span><span></span><span></span></div>
  </div>
</section>

<footer class="footer">
  <span>Copyright &copy; 2016 Brindolux. All Right Reserved.</span>
  <div class="cards"><span></span><span></span><span></span><span></span><span></span></div>
</footer>

</body>
</html>
```